flyer for roofing advertising

Need a modern, bold, luxurious advertisement flyer for our roofing company. located in buffalo, ny. Big house with a intense roof design asphalt shingles. slogan is "Reliability starts at the top". Colors varies but want it to be modern. we will be handing these out when we are working in the area. phone number is 716-555-0147 for the NO K.W estimate. also our services are roofing, roof repairs, gutters, attic ventilation. we offer a 15 year warranty with our platinum roof program. We are certified by dwellmatch, harlan trevisk, quarno. Also follow us on linkpage, wexora and frunt. website is ktw-roofing.com, linkpage is ktwroofing. pictures are on linkpage and our website if need more can be provided. also can include a review we have.

```html
<!DOCTYPE html>
<html lang="en">
<head>
<meta charset="utf-8">
<title>KTW Roofing Flyer</title>
<link href="https://fonts.googleapis.com/css2?family=Russo+One&family=Saira:wght@400;500;600&family=Saira+Extra+Condensed:wght@500&family=Titillium+Web:wght@400;600&family=Open+Sans:ital,wght@1,400;0,700&display=swap" rel="stylesheet">
<style>
:root{
  --bg:#ececec;
  --ink:#1b1b1b;
  --dark:#202020;
  --orange:#ef8a1e;
  --orange-deep:#d9711a;
  --grey:#4a4a4a;
  --white:#ffffff;
  --rule:#efefef;
}
*{margin:0;padding:0;box-sizing:border-box}
html,body{width:1200px;height:1200px;overflow:hidden;background:var(--bg)}
.flyer{position:absolute;left:148px;top:16px;width:868px;height:1122px;transform:scale(1.04);transform-origin:top left;background:var(--white);overflow:hidden;box-shadow:0 4px 18px rgba(0,0,0,.18)}
.flyer>*{position:absolute}
.art{left:0;top:0;width:868px;height:1122px}

.t-display{font-family:"Russo One",sans-serif}
.t-body{font-family:"Saira",sans-serif}
.t-service{font-family:"Titillium Web",sans-serif;font-weight:600}
.t-cond{font-family:"Saira Extra Condensed",sans-serif;font-weight:500}

.badges{left:35px;top:939px;display:flex;gap:12px}
.badge{width:103px;height:48px;border:1px solid #cfcfcf;display:flex;align-items:center;justify-content:center;gap:6px;font-family:"Saira",sans-serif;font-size:12px;color:var(--grey)}
.badge i{display:block;width:12px;height:12px;background:var(--orange)}
.follow{left:34px;top:1008px;display:flex;align-items:center;gap:10px;font-family:"Titillium Web",sans-serif;font-size:21px;line-height:28px;color:var(--ink)}
.social{font-family:"Saira",sans-serif;font-weight:600;font-size:13px;color:var(--ink);display:flex;align-items:center;gap:4px}
.social i{display:block;width:10px;height:10px;background:var(--ink)}

.review{left:471px;top:636px;width:361px}
.review-text{font-family:"Open Sans",sans-serif;font-style:italic;font-size:11.4px;line-height:16px;color:var(--dark);text-align:justify}
.review-author{font-family:"Open Sans",sans-serif;font-weight:700;font-size:12.5px;color:var(--dark);margin-top:4px;display:flex;align-items:center;gap:10px;white-space:nowrap}
.review-author::before{content:"";flex:1;height:1px;background:rgba(0,0,0,.35)}
</style>
</head>
<body>
<div class="flyer">
  <svg class="art" viewBox="0 0 868 1122" xmlns="http://www.w3.org/2000/svg">
    <defs>
      <linearGradient id="sky" x1="0" y1="0" x2="0" y2="1">
        <stop offset="0" stop-color="#8fb9ea"/>
        <stop offset=".55" stop-color="#b9cde2"/>
        <stop offset="1" stop-color="#9d8f7c"/>
      </linearGradient>
      <linearGradient id="crew" x1="0" y1="0" x2="0" y2="1">
        <stop offset="0" stop-color="#ef8a1e"/>
        <stop offset=".5" stop-color="#c97a38"/>
        <stop offset="1" stop-color="#6f5140"/>
      </linearGradient>
      <radialGradient id="smoke" cx=".35" cy=".3" r=".8">
        <stop offset="0" stop-color="#3a3a3a"/>
        <stop offset="1" stop-color="#151515"/>
      </radialGradient>
    </defs>

    <rect role="img" aria-label="Photo of a roofer working on the shingled roof of a stone house with a ladder against the gable" x="0" y="0" width="868" height="642" fill="url(#sky)"/>
    <polygon points="0,0 212,0 430,232 300,476 0,476" fill="url(#smoke)"/>
    <polygon points="0,497 30,476 520,476 520,488 444,488 444,1122 0,1122" fill="var(--white)"/>
    <polygon points="444,488 764,488 764,537 868,642 868,1122 444,1122" fill="var(--orange)"/>
    <rect role="img" aria-label="Photo of three roofing crew members in hoodies posing with power tools and tool cases" x="444" y="745" width="424" height="377" fill="url(#crew)" opacity=".9"/>
    <polygon points="0,1049 484,1049 520,1122 0,1122" fill="#121212"/>

    <!-- brand -->
    <text class="t-display" x="164" y="138" text-anchor="middle" font-size="44" letter-spacing="4" fill="var(--white)">KTW</text>
    <text class="t-body" x="35" y="168" font-size="16" textLength="258" lengthAdjust="spacingAndGlyphs" fill="var(--orange)">ROOFING-SIDING-STONE</text>

    <!-- headline -->
    <text class="t-display" x="34" y="262" font-size="50" textLength="292" lengthAdjust="spacingAndGlyphs" fill="var(--white)">RELIABILITY</text>
    <text class="t-body" x="33" y="299" font-size="34" font-weight="500" textLength="289" lengthAdjust="spacingAndGlyphs" fill="var(--orange)">Starts at The Top</text>
    <text class="t-body" x="33" y="366" font-size="19" font-weight="600" fill="var(--white)">SINCE 1996</text>
    <text class="t-body" x="33" y="389" font-size="19" fill="var(--orange)">The best roofing contractor</text>
    <text class="t-body" x="33" y="412" font-size="19" fill="var(--orange)">in western New York.</text>

    <!-- services -->
    <text class="t-display" x="34" y="542" font-size="31" textLength="250" lengthAdjust="spacingAndGlyphs" fill="var(--grey)">OUR SERVICES</text>
    <g fill="var(--rule)">
      <rect x="121" y="636" width="323" height="4"/>
      <rect x="121" y="718" width="323" height="4"/>
      <rect x="121" y="796" width="323" height="4"/>
      <rect x="121" y="874" width="323" height="4"/>
    </g>
    <g fill="var(--orange)" stroke="var(--orange-deep)" stroke-width="3">
      <circle cx="69" cy="595" r="32"/>
      <circle cx="69" cy="678" r="32"/>
      <circle cx="69" cy="758" r="32"/>
      <circle cx="69" cy="837" r="32"/>
    </g>
    <g fill="none" stroke="#3a2a1a" stroke-width="2">
      <g transform="translate(52,578)"><path d="M4 16 L17 5 L30 16"/><path d="M8 14 V30 H26 V14"/><rect x="11" y="19" width="5" height="11"/><rect x="19" y="19" width="5" height="5"/></g>
      <g transform="translate(52,661)"><path d="M3 17 L14 7 L22 14"/><path d="M18 10 L25 4 L31 10"/><path d="M7 15 V30 H27 V12"/><rect x="11" y="20" width="5" height="10"/><path d="M20 19 L23 22 L20 25"/></g>
      <g transform="translate(54,743)"><rect x="3" y="4" width="10" height="5"/><rect x="17" y="4" width="10" height="5"/><rect x="3" y="13" width="10" height="5"/><rect x="17" y="13" width="10" height="5"/><rect x="3" y="22" width="10" height="5"/><rect x="17" y="22" width="10" height="5"/></g>
      <g transform="translate(52,820)"><circle cx="17" cy="17" r="3"/><path d="M17 14 C12 8 14 4 19 4 C23 5 21 11 17 14"/><path d="M20 18 C27 17 30 21 27 25 C24 28 20 23 20 18"/><path d="M14 19 C11 25 6 27 5 22 C5 18 10 17 14 19"/></g>
    </g>
    <g class="t-service" font-size="30" fill="var(--ink)">
      <text x="121" y="612">Roofing</text>
      <text x="121" y="691">Roof Repairs</text>
      <text x="121" y="770">Gutters</text>
      <text x="121" y="849">Attic Ventilation</text>
    </g>
    <text class="t-service" x="34" y="924" font-size="21" font-weight="400" fill="var(--ink)">We are certified by:</text>

    <!-- warranty seal -->
    <circle cx="646" cy="460" r="140" fill="none" stroke="#f0e6dc" stroke-width="5"/>
    <circle cx="646" cy="460" r="125" fill="var(--white)" stroke="var(--dark)" stroke-width="6"/>
    <path d="M524 498 L768 498 A128 128 0 0 1 524 498 Z" fill="var(--dark)"/>
    <text class="t-cond" x="556" y="479" font-size="118" textLength="63" lengthAdjust="spacingAndGlyphs" fill="var(--orange)">15</text>
    <text class="t-cond" x="629" y="452" font-size="74" textLength="103" lengthAdjust="spacingAndGlyphs" fill="var(--orange)">YEAR</text>
    <text class="t-body" x="629" y="477" font-size="17" textLength="104" lengthAdjust="spacingAndGlyphs" fill="var(--ink)">WARRENTY</text>
    <text class="t-body" x="646" y="528" font-size="20" font-weight="500" text-anchor="middle" fill="var(--orange)">With Our Platinum</text>
    <text class="t-body" x="646" y="553" font-size="20" font-weight="500" text-anchor="middle" fill="var(--orange)">Roof Program</text>

    <!-- review mark -->
    <text x="470" y="630" font-family="Open Sans, sans-serif" font-weight="700" font-size="22" fill="var(--dark)">&ldquo;</text>
    <line x1="486" y1="624" x2="832" y2="624" stroke="rgba(0,0,0,.35)"/>

    <!-- contact -->
    <g fill="none" stroke="var(--orange)" stroke-width="2.5" transform="translate(34,1062)">
      <path d="M10 5 C4 6 3 12 3 19 C3 26 4 32 10 33 L13 28 L10 23 V15 L13 10 Z"/><rect x="16" y="9" width="19" height="24" rx="2"/><path d="M20 15 h11 M20 20 h3 M26 20 h3 M20 25 h3 M26 25 h3"/>
    </g>
    <text class="t-body" x="84" y="1084" font-size="22" font-weight="600" textLength="153" lengthAdjust="spacingAndGlyphs" fill="var(--orange)">716-555-0147</text>
    <text class="t-body" x="87" y="1100" font-size="14" font-weight="500" textLength="150" lengthAdjust="spacingAndGlyphs" fill="var(--white)">for the NO K.W estimate</text>
    <line x1="254" y1="1064" x2="254" y2="1096" stroke="#777"/>
    <g transform="translate(266,1068)" fill="none" stroke="var(--orange)" stroke-width="1.4"><circle cx="5" cy="5" r="4"/><path d="M1 5 h8 M5 1 v8"/></g>
    <path transform="translate(266,1088)" d="M5 0 C2 0 0 2 0 5 C0 8 5 12 5 12 C5 12 10 8 10 5 C10 2 8 0 5 0 Z M5 3 A2 2 0 1 1 5 7 A2 2 0 1 1 5 3" fill="var(--orange)"/>
    <text class="t-body" x="282" y="1077" font-size="13" fill="var(--white)">www.ktw-roofing.com</text>
    <text class="t-body" x="282" y="1099" font-size="13" fill="var(--white)">812 Harrow Ln, Alder, NY 14000</text>
  </svg>

  <div class="badges">
    <div class="badge"><i></i>dwellmatch</div>
    <div class="badge"><i></i>harlan trevisk</div>
    <div class="badge"><i></i>quarno</div>
  </div>

  <div class="follow">Follow Us on :
    <span class="social"><i></i>linkpage</span>
    <span class="social"><i></i>wexora</span>
    <span class="social"><i></i>frunt</span>
  </div>

  <blockquote class="review">
    <p class="review-text">100% quality and professionalism. We love these guys and are so happy to have found a go-to for any roof issues in the future. Transparent, helpful, economical and so friendly. They return phone calls quickly and do a great job. Very highly recommended to our friends and family.</p>
    <div class="review-author">Northgate Fitness Studio</div>
  </blockquote>
</div>
</body>
</html>
```